Infographic for a Christian church discipleship pathway

We need to take a fairly complex program that helps people in a Baptist church follow Jesus, and turn it into a simple graphic. This graphic does not have to explain the whole program, web pages and print materials will do that. But, it should be something that people see and understand what it is quickly. The attached graphic is only to give the key words and general direction of the program. It should not serve as a design guide. In other words, we want to see some other ideas how this information can be imparted graphically with concision and creativity. It's important to note, the categories at the top (pray daily, read daily, gather weekly) are first steps, starting points....one shouldn't move forward until they've incorporated these things into their life. However, the categories that follow (study, connect, serve, etc) are not necessarily steps to take in sequential order.

The diagrams we've provided are not what we expect. They are only to explain the program. Here is a verbal description: The motto of our church is "A Ready Church" (ready to serve, ready to love, ready for when Jesus returns). There are four words that describe a ready church member: FOCUSED on the return of Christ, FAITHFUL in a daily relationship with Jesus, PREPARED for any opportunity to be a supernatural vessel of God's worK, LOOKING to invite others into God's family. The first two are God's Work in Me (Focused and faithful); the second two are God's Work Through me (Prepared, looking). Please use those two things as you wish (Focused faithful prepared looking; and God's word in and through me). If they are clarifying, please use. If not, you don't have to use.

Additionally, the strategies we employ to be "a ready church" are 1. Prayer 2. God's Word, and 3. Biblical Community. (So, in other words, these three things help us be a people who is focused, faithful, prepared, and looking....which is a ready church.

To provide some information how we will build this out: this graphic will be used in print and digital content. The digital content will allow people to click on each category to access training and resources associated with that discipline. (Fasting, reflecting, etc).

www.kwm.parish

Target Market(s)

35-50

Industry/Entity Type

Religious

Other font styles liked:
• Lato and/or Cambria

Requirements
Must have
• Fonts: lato, cambria. Colors#: 373E41, ebebe8, #a69677. Accent Colors: 80401D, #4e5730, #a5bac8
Nice to have
• A designer who has an understanding of what it means to incorporate the spiritual disciplines of the Christian faith into their life.

```html
<!DOCTYPE html>
<html lang="en">
<head>
<meta charset="utf-8">
<title>A Ready Church – Discipleship Pathway</title>
<link href="https://fonts.googleapis.com/css2?family=Outfit:wght@300;400;600;700;800&display=swap" rel="stylesheet">
<style>
:root{
  --charcoal:#373e41;
  --paper:#ffffff;
  --olive:#5c6343;
  --olive-band:#6b704c;
  --olive-body:#dddcd5;
  --slate-band:#97a6b8;
  --slate-text:#8e9db0;
  --slate-body:#d3e0ee;
  --sage-band:#b4c0c0;
  --sage-text:#a8b6b8;
  --sage-body:#d6dcdd;
  --ink:#2f3437;
  --pill-border:#8e9aa8;
  --arrow:#373e41;
}
*{box-sizing:border-box;margin:0;padding:0}
html,body{width:1200px;height:900px;overflow:hidden;background:var(--paper)}
body{position:relative;font-family:"Outfit",sans-serif;color:var(--ink)}
.side-panel{position:absolute;left:0;top:0;width:338px;height:900px;
  background:linear-gradient(180deg,var(--charcoal) 0%,#474d50 35%,#55595b 60%,#3a3f42 100%)}
.brand{position:absolute;left:80px;top:104px;display:flex;align-items:center;gap:14px}
.brand-mark{width:34px;height:34px;border-radius:50%;background:#fff;flex:none}
.brand-name{font-family:"Outfit",sans-serif;font-weight:600;color:#fff;font-size:21px;line-height:24px;letter-spacing:2px}
.start-here{position:absolute;left:118px;top:354px;color:#fff;font-weight:600;font-size:25px;letter-spacing:5px}
.start-arrow{position:absolute;left:352px;top:357px}
.pill{position:absolute;left:68px;width:328px;height:108px;border-radius:54px;background:#fff;
  border:1.5px solid var(--pill-border);text-align:center;padding-top:30px}
.pill h3{font-weight:700;font-size:23px;letter-spacing:-.3px;color:var(--ink)}
.pill p{font-weight:300;font-size:15px;margin-top:2px}
.pill-in{top:431px}.pill-through{top:663px}
.title{position:absolute;left:430px;top:74px;width:690px;text-align:center;
  font-weight:800;font-size:80px;letter-spacing:-1.5px;color:var(--charcoal);line-height:1}
.tagline{position:absolute;left:430px;top:150px;width:690px;text-align:center;font-weight:700;font-size:15.5px;
  letter-spacing:2.3px;color:var(--olive)}
.strategy{position:absolute;top:0;width:223px;height:900px}
.strategy-head{position:absolute;top:215px;left:-20px;width:263px;text-align:center}
.strategy-head h2{font-weight:700;font-size:19px;letter-spacing:-.2px}
.strategy-head p{font-weight:300;font-size:12px;line-height:15px;margin-top:2px}
.column{position:absolute;top:330px;left:0;width:223px;height:491px;border-radius:20px;overflow:hidden}
.band{height:52px;color:#fff;font-weight:700;font-size:16.5px;text-align:center;padding-top:26px;letter-spacing:-.2px}
.badge{position:absolute;top:288px;left:75px;width:74px;height:74px;border-radius:50%;background:#f2f2f2;
  border:2px solid #e2e2e2}
.badge span{position:absolute;left:6px;top:6px;width:58px;height:58px;border-radius:50%;background:#fff;
  border:3px solid var(--ring);text-align:center;line-height:52px;font-weight:800;font-size:34px;color:var(--charcoal)}
.step{position:absolute;left:9px;width:205px;border-radius:6px;text-align:center;font-weight:400;font-size:16px;
  color:var(--ink);background:linear-gradient(180deg,rgba(255,255,255,.25),rgba(0,0,0,.04));
  box-shadow:0 2px 3px rgba(0,0,0,.06)}
.s1{top:57px;height:86px;padding-top:31px}
.s2{top:150px;height:105px;padding-top:40px}
.s3{top:262px;height:106px;padding-top:41px}
.s4{top:379px;height:101px;padding-top:36px}
.flow{position:absolute;left:104px}
.f1{top:146px}.f2{top:260px}.f3{top:372px}
.prayer{left:427px}.prayer h2{color:var(--slate-text)}.prayer .band{background:var(--slate-band)}
.prayer .column{background:var(--slate-body)}.prayer .badge{--ring:#b8c3d0}
.word{left:667px}.word h2{color:var(--olive)}.word .band{background:var(--olive-band)}
.word .column{background:var(--olive-body)}.word .badge{--ring:var(--olive-band)}
.community{left:903px}.community h2{color:var(--sage-text)}.community .band{background:var(--sage-band)}
.community .column{background:var(--sage-body)}.community .badge{--ring:#c3cccc}
</style>
</head>
<body>
<div class="side-panel" role="img" aria-label="Photograph of a church sanctuary interior with arched nave, rose window and altar, in dark grey tones"></div>
<div class="brand"><span class="brand-mark"></span><span class="brand-name">KINGSWOOD<br>CHAPEL</span></div>
<div class="start-here">START HERE</div>
<svg class="start-arrow" width="48" height="26" viewBox="0 0 48 26" aria-hidden="true">
  <rect x="0" y="7" width="3" height="12" fill="#373e41"/><rect x="6" y="7" width="3" height="12" fill="#373e41"/>
  <rect x="12" y="8" width="16" height="10" fill="#373e41"/><polygon points="27,0 46,13 27,26" fill="#373e41"/>
</svg>
<div class="pill pill-in"><h3>Focused. Faithful</h3><p>God’s Work in me</p></div>
<div class="pill pill-through"><h3>Prepared. Looking</h3><p>God’s Work thorough me</p></div>

<h1 class="title">A READY CHURCH</h1>
<div class="tagline">READY TO SERVE, READY TO LOVE, READY FOR WHEN JESUS RETURNS</div>

<section class="strategy prayer">
  <div class="strategy-head"><h2>PRAYER</h2><p>Become a person devoted to<br>prayer each day of your life</p></div>
  <div class="column"><div class="band">PRAY DAILY</div>
    <div class="step s1">REST</div><div class="step s2">REFLECT</div><div class="step s3">FAST</div><div class="step s4">INTERCEDE</div>
    <svg class="flow f1" width="14" height="28" viewBox="0 0 14 28"><rect x="4" y="0" width="6" height="2" fill="#373e41"/><rect x="4" y="4" width="6" height="2" fill="#373e41"/><rect x="4" y="8" width="6" height="8" fill="#373e41"/><polygon points="0,15 14,15 7,27" fill="#373e41"/></svg>
    <svg class="flow f2" width="14" height="28" viewBox="0 0 14 28"><rect x="4" y="0" width="6" height="2" fill="#373e41"/><rect x="4" y="4" width="6" height="2" fill="#373e41"/><rect x="4" y="8" width="6" height="8" fill="#373e41"/><polygon points="0,15 14,15 7,27" fill="#373e41"/></svg>
    <svg class="flow f3" width="14" height="28" viewBox="0 0 14 28"><rect x="4" y="0" width="6" height="2" fill="#373e41"/><rect x="4" y="4" width="6" height="2" fill="#373e41"/><rect x="4" y="8" width="6" height="8" fill="#373e41"/><polygon points="0,15 14,15 7,27" fill="#373e41"/></svg>
  </div>
  <div class="badge"><span>P</span></div>
</section>

<section class="strategy word">
  <div class="strategy-head"><h2>GOD’S WORD</h2><p>Build a daily habit of<br>beholding God in his Word</p></div>
  <div class="column"><div class="band">GOD’S WORD</div>
    <div class="step s1">STUDY</div><div class="step s2">MEMORIZE</div><div class="step s3">TEACH</div><div class="step s4">PROCLAIM</div>
    <svg class="flow f1" width="14" height="28" viewBox="0 0 14 28"><rect x="4" y="0" width="6" height="2" fill="#373e41"/><rect x="4" y="4" width="6" height="2" fill="#373e41"/><rect x="4" y="8" width="6" height="8" fill="#373e41"/><polygon points="0,15 14,15 7,27" fill="#373e41"/></svg>
    <svg class="flow f2" width="14" height="28" viewBox="0 0 14 28"><rect x="4" y="0" width="6" height="2" fill="#373e41"/><rect x="4" y="4" width="6" height="2" fill="#373e41"/><rect x="4" y="8" width="6" height="8" fill="#373e41"/><polygon points="0,15 14,15 7,27" fill="#373e41"/></svg>
    <svg class="flow f3" width="14" height="28" viewBox="0 0 14 28"><rect x="4" y="0" width="6" height="2" fill="#373e41"/><rect x="4" y="4" width="6" height="2" fill="#373e41"/><rect x="4" y="8" width="6" height="8" fill="#373e41"/><polygon points="0,15 14,15 7,27" fill="#373e41"/></svg>
  </div>
  <div class="badge"><span>G</span></div>
</section>

<section class="strategy community">
  <div class="strategy-head"><h2>BIBLICAL COMMUNITY</h2><p>Engage deeply in christian<br>community</p></div>
  <div class="column"><div class="band">BIBLICAL COMMUNITY</div>
    <div class="step s1">CONNECT</div><div class="step s2">LEARN</div><div class="step s3">GIVE</div><div class="step s4">SERVE</div>
    <svg class="flow f1" width="14" height="28" viewBox="0 0 14 28"><rect x="4" y="0" width="6" height="2" fill="#373e41"/><rect x="4" y="4" width="6" height="2" fill="#373e41"/><rect x="4" y="8" width="6" height="8" fill="#373e41"/><polygon points="0,15 14,15 7,27" fill="#373e41"/></svg>
    <svg class="flow f2" width="14" height="28" viewBox="0 0 14 28"><rect x="4" y="0" width="6" height="2" fill="#373e41"/><rect x="4" y="4" width="6" height="2" fill="#373e41"/><rect x="4" y="8" width="6" height="8" fill="#373e41"/><polygon points="0,15 14,15 7,27" fill="#373e41"/></svg>
    <svg class="flow f3" width="14" height="28" viewBox="0 0 14 28"><rect x="4" y="0" width="6" height="2" fill="#373e41"/><rect x="4" y="4" width="6" height="2" fill="#373e41"/><rect x="4" y="8" width="6" height="8" fill="#373e41"/><polygon points="0,15 14,15 7,27" fill="#373e41"/></svg>
  </div>
  <div class="badge"><span>B</span></div>
</section>
</body>
</html>
```